Business Card Design for an Investment Company

We need a business card design for our private investment company, called Ashbourne Partners. Ashbourne Partners is an investments partnership that aims to acquire shares in listed companies with a view to influencing those companies through active dialogue in order to improve their value. We need designs that use the logo colors (blue, grey, white), we need both English and Arabic on the business cards (can be on one side or 2 sides). The final logo should communicate professionalism, conservatism (nothing too fancy or too cheesy), that we are smart, conservative and old school.

Target Market(s)

Investment companies

Industry/Entity Type

Investment

Contact Information for Business Card

Khalid Yousef Rumaithi
Senior Executive Officer

Palm Terrace 07, Level 3, Office 215/12
HLMZ

+9714987650
krumaithi@ashbournepartners.com
www.ashbournepartners.com

Requirements
Must have
• Logo to be placed on the left hand side of the business card
• for the Arabic, we only need to have the name and title so it can be accomodated on one side so we can have the other side with full color and logo. The arabic that needs to be used is the below:
• خالد يوسف الرميثي
• المدير التنفيدي

```html
<!DOCTYPE html>
<html lang="en">
<head>
<meta charset="utf-8">
<title>Ashbourne Partners – Business Card</title>
<link rel="stylesheet" href="https://fonts.googleapis.com/css2?family=Open+Sans:wght@300;400;600;700;800&family=Noto+Kufi+Arabic:wght@300;700&display=swap">
<style>
  :root {
    --brand-blue: #006a9e;
    --brand-grey: #58595b;
    --line-grey: #4a4a4c;
    --paper-white: #ffffff;
    --stage: #2a2a2c;
    --text-light: #f2f2f2;
  }
  * { box-sizing: border-box; margin: 0; padding: 0; }
  html, body { width: 1200px; height: 925px; overflow: hidden; }
  body {
    background: var(--stage);
    font-family: "Open Sans", Arial, sans-serif;
    position: relative;
  }
  .card {
    position: absolute;
    width: 520px;
    height: 297px;
    top: 314px;
    overflow: hidden;
  }
  .card-front { left: 50px; background: var(--paper-white); }
  .card-back { left: 630px; background: var(--brand-grey); }

  /* Front */
  .front-rule-top {
    position: absolute; top: 70px; right: 0; width: 205px; height: 2px;
    background: var(--line-grey);
  }
  .front-rule-bottom {
    position: absolute; bottom: 66px; left: 0; width: 190px; height: 2px;
    background: var(--brand-blue);
  }
  .front-logo {
    position: absolute; left: 74px; top: 116px;
    display: flex; align-items: center; gap: 10px;
  }
  .logo-square { width: 22px; height: 22px; background: var(--brand-grey); }
  .logo-name {
    font-size: 34px; font-weight: 700; letter-spacing: -0.5px;
    color: var(--brand-blue); line-height: 1;
  }
  .front-web {
    position: absolute; left: 208px; top: 176px;
    font-size: 14px; letter-spacing: 1.2px; color: var(--brand-grey);
  }

  /* Back */
  .holder { position: absolute; left: 30px; top: 28px; color: var(--paper-white); }
  .holder-name { font-size: 18px; font-weight: 700; }
  .holder-title { font-size: 12.5px; font-weight: 300; margin-top: 2px; color: var(--text-light); }
  .holder-arabic {
    position: absolute; right: 30px; top: 24px;
    direction: rtl; text-align: right; color: var(--paper-white);
    font-family: "Noto Kufi Arabic", "Open Sans", sans-serif;
  }
  .holder-arabic .holder-name { font-size: 16px; line-height: 1.5; }
  .holder-arabic .holder-title { font-size: 12px; margin-top: 0; }
  .contact {
    position: absolute; left: 252px; top: 82px;
    font-size: 12.5px; line-height: 17px; color: var(--text-light); font-weight: 300;
    list-style: none;
  }
  .contact li { display: flex; align-items: center; gap: 6px; }
  .contact .address { display: block; }
  .contact svg { width: 11px; height: 11px; flex: none; }
  .band-divider {
    position: absolute; left: 0; right: 0; bottom: 88px; height: 4px;
    background: var(--paper-white);
  }
  .band {
    position: absolute; left: 0; right: 0; bottom: 0; height: 84px;
    background: var(--brand-blue);
    display: flex; align-items: center; padding-left: 30px; gap: 10px;
  }
  .band .logo-square { background: var(--paper-white); }
  .band .logo-name { color: var(--paper-white); font-size: 30px; }
</style>
</head>
<body>
  <section class="card card-front" aria-label="Card front">
    <div class="front-rule-top"></div>
    <div class="front-logo">
      <span class="logo-name">Ashbourne Partners</span>
      <span class="logo-square"></span>
    </div>
    <p class="front-web">www.ashbournepartners.com</p>
    <div class="front-rule-bottom"></div>
  </section>

  <section class="card card-back" aria-label="Card back">
    <div class="holder">
      <p class="holder-name">Khalid Yousef Rumaithi</p>
      <p class="holder-title">Senior Executive Officer</p>
    </div>
    <div class="holder-arabic" lang="ar">
      <p class="holder-name">خالد يوسف الرميثي</p>
      <p class="holder-title">المدير التنفيدي</p>
    </div>
    <ul class="contact">
      <li class="address">Ashbourne Partners<br>Palm Terrace 07, Level 3,<br>Office 215/12 HLMZ</li>
      <li>
        <svg viewBox="0 0 12 12" aria-hidden="true"><path d="M2 1h3l1 3-1.5 1a7 7 0 0 0 2.5 2.5L8 6l3 1v3c0 .6-.4 1-1 1A9 9 0 0 1 1 2c0-.6.4-1 1-1z" fill="#fff"/></svg>
        +9714987650
      </li>
      <li>
        <svg viewBox="0 0 12 12" aria-hidden="true"><rect x="0.5" y="2" width="11" height="8" fill="#fff"/><path d="M0.5 2l5.5 4.5L11.5 2" fill="none" stroke="#58595b" stroke-width="1"/></svg>
        krumaithi@ashbournepartners.com
      </li>
      <li>
        <svg viewBox="0 0 12 12" aria-hidden="true"><circle cx="6" cy="6" r="5.5" fill="#fff"/><path d="M0.5 6h11M6 .5c-3 3-3 8 0 11M6 .5c3 3 3 8 0 11" fill="none" stroke="#58595b" stroke-width=".8"/></svg>
        www.ashbournepartners.com
      </li>
    </ul>
    <div class="band-divider"></div>
    <div class="band">
      <span class="logo-name">Ashbourne Partners</span>
      <span class="logo-square"></span>
    </div>
  </section>
</body>
</html>
```